Book Cover Design

Design with title UNWAVERING
Subtitle: Ways to Kindle the Spark of Resolve
Author Name: Carla Jean Morrow
Put DAILY MERIDIAN BESTSELLER at top
Shimmer design, see inspirational images attached

```html
<!DOCTYPE html>
<html lang="en">
<head>
<meta charset="UTF-8">
<title>Unwavering — Book Cover</title>
<link rel="stylesheet" href="https://fonts.googleapis.com/css2?family=Saira+Condensed:wght@500;600;700&family=Titillium+Web:wght@600&display=swap">
<style>
  :root {
    --page-bg: #f4f2f3;
    --blush-top: #e6b2cf;
    --blush-mid: #f4cfdb;
    --rose-soft: #f0d4d6;
    --peach-low: #e9c9ae;
    --gold-glow: #f6e2c4;
    --spark: rgba(255, 246, 225, 0.85);
    --title-stroke: #9a86f0;
    --ink: #111014;
  }
  * { margin: 0; padding: 0; box-sizing: border-box; }
  html, body {
    width: 1200px;
    height: 1200px;
    overflow: hidden;
    background: var(--page-bg);
  }
  .canvas {
    position: relative;
    width: 1200px;
    height: 1200px;
    display: flex;
    align-items: center;
    justify-content: center;
  }
  .book-cover {
    position: relative;
    width: 800px;
    height: 1130px;
    overflow: hidden;
    box-shadow: 0 18px 40px rgba(0,0,0,0.18);
  }
  .shimmer-backdrop {
    position: absolute;
    inset: 0;
    background:
      radial-gradient(circle 26px at 62% 50%, var(--spark), transparent 100%),
      radial-gradient(circle 20px at 70% 58%, var(--spark), transparent 100%),
      radial-gradient(circle 22px at 66% 64%, var(--spark), transparent 100%),
      radial-gradient(circle 18px at 76% 68%, var(--spark), transparent 100%),
      radial-gradient(circle 16px at 44% 62%, var(--spark), transparent 100%),
      radial-gradient(circle 14px at 36% 70%, var(--spark), transparent 100%),
      radial-gradient(circle 18px at 58% 72%, var(--spark), transparent 100%),
      radial-gradient(ellipse 60% 40% at 58% 28%, rgba(255,242,240,0.75), transparent 70%),
      radial-gradient(ellipse 90% 30% at 50% 95%, var(--gold-glow), transparent 80%),
      radial-gradient(ellipse 70% 22% at 50% 80%, rgba(250,232,205,0.8), transparent 80%),
      linear-gradient(172deg, var(--blush-top) 0%, var(--blush-mid) 40%, var(--rose-soft) 65%, var(--peach-low) 100%);
  }
  .bestseller-line {
    position: absolute;
    top: 48px;
    left: 0;
    width: 100%;
    text-align: center;
    white-space: nowrap;
    font-family: 'Saira Condensed', sans-serif;
    font-weight: 600;
    font-size: 44px;
    letter-spacing: 0.14em;
    color: var(--ink);
  }
  .title-vertical {
    position: absolute;
    left: 0;
    top: 0;
    width: 800px;
    height: 1130px;
  }
  .title-vertical text {
    font-family: 'Saira Condensed', sans-serif;
    font-weight: 500;
    font-size: 180px;
    fill: none;
    stroke: var(--title-stroke);
    stroke-width: 1.6;
  }
  .subtitle {
    position: absolute;
    top: 880px;
    left: 0;
    width: 100%;
    text-align: center;
    white-space: nowrap;
    font-family: 'Titillium Web', sans-serif;
    font-weight: 600;
    font-size: 32px;
    color: var(--ink);
  }
  .author-name {
    position: absolute;
    top: 928px;
    left: 0;
    width: 100%;
    text-align: center;
    white-space: nowrap;
    font-family: 'Saira Condensed', sans-serif;
    font-weight: 700;
    font-size: 86px;
    letter-spacing: 0.04em;
    color: var(--ink);
  }
</style>
</head>
<body>
  <main class="canvas">
    <article class="book-cover">
      <div class="shimmer-backdrop" role="img" aria-label="Soft pink to peach shimmering glitter background with golden bokeh lights"></div>
      <p class="bestseller-line">DAILY MERIDIAN BESTSELLER</p>
      <svg class="title-vertical" viewBox="0 0 800 1130" aria-label="UNWAVERING">
        <text x="0" y="0" transform="translate(420 820) rotate(-90)" textLength="630" lengthAdjust="spacingAndGlyphs" dominant-baseline="middle">UNWAVERING</text>
      </svg>
      <p class="subtitle">Ways to Kindle the Spark of Resolve</p>
      <h1 class="author-name">CARLA JEAN MORROW</h1>
    </article>
  </main>
</body>
</html>
```